Emerging automotive detailing business

I am starting a small automotive detailing business in hopes of becoming a well-known detailer to work on high end cars. I would like a card to reflect the high quality and time I put into my work. The name of the company is Brightmere Detailing. I feel like it represents racecars getting off the line at the drag strip as well as an innuendo of "Off the Charts". I do minor paint correction such as clay barring, multi-step buffing and polishing, waxing, hand washes, etc. I am always striving to learn more and improve my work. My goal is to have total customer satisfaction. This is a female run business but I do not want it to be very girly. Elegant is okay! I have pictures of my personal kestrel attached, they do not need to be incorporated but if you can think of a cool way to use 1 or all of them, go for it!

Target Market(s)

Anyone that owns a vehicle. Preferably high end vehicles such as Valdren, Castavelli and Moretto but I will also happily work on any car, truck or suv no matter what brand.

Industry/Entity Type

Automotive

Contact Information for Business Card

Brightmere Detailing
Nora Pellworth
4715 Quillbrook Rd
Ashcombe VT 05871
Cell phone- call/text- 802-555-0148
email- brightmeredetails@example.com
Instagram: @brightmeredetailing
Facebook: facebook.example/brightmeredetailing

Requirements
Must have
• Business name, my name, address, phone number. Listing that I do minor paint correction such as clay barring, multi-step buffing and polishing, waxing, hand washes, interior cleaning, and more. (This last part was in nice to haves but I have realized that I do really want it, so I moved it to must haves.) I want something that is different and eye-catching to my customers. Some people have done this very well with cards already submitted to me, but a lot have not. I didn't mess with the "look and feel bars" much because because I am pretty open to the overall design as long as it is not your basic run of the mill design.
Nice to have
• Something car related. Maybe an appointment time/date line. I do not have a logo, but if you would like to design one and incorporate it, that would be amazing!
Should not have
• Purple and Pink colors. Boring, basic, normal card.

```html
<!DOCTYPE html>
<html lang="en">
<head>
<meta charset="utf-8">
<title>Brightmere Detailing – Business Card</title>
<link rel="stylesheet" href="https://fonts.googleapis.com/css2?family=Jura:wght@300;400&family=Quicksand:wght@400;500&display=swap">
<style>
  :root {
    --backdrop: #f1e300;
    --card-black: #050505;
    --ink: #1c1c1c;
    --ink-soft: #2e2e2e;
    --title-light: #e6e6e6;
  }
  * { box-sizing: border-box; margin: 0; padding: 0; }
  html, body {
    width: 1200px; height: 800px; overflow: hidden;
    background: var(--backdrop);
  }
  .stage {
    position: relative; width: 1200px; height: 800px;
    display: flex; align-items: center; justify-content: center; gap: 40px;
  }
  .card {
    position: relative; width: 540px; height: 300px;
    background: var(--card-black); overflow: hidden;
    box-shadow: 0 10px 24px rgba(0,0,0,0.25);
  }
  .card-art { position: absolute; inset: 0; width: 100%; height: 100%; }
  .brand-title {
    position: absolute; top: 26px; left: 0; right: 0;
    text-align: center; color: var(--title-light);
    font-family: "Jura", sans-serif; font-weight: 300;
    font-size: 44px; line-height: 52px; letter-spacing: 3px;
  }
  .holder-name {
    position: absolute; left: 26px; top: 196px;
    font-family: "Quicksand", sans-serif; font-weight: 500;
    font-size: 18px; color: var(--ink); letter-spacing: 0.5px;
  }
  .holder-address {
    position: absolute; left: 26px; top: 243px;
    font-family: "Quicksand", sans-serif; font-size: 14px;
    line-height: 19px; color: var(--ink-soft);
  }
  .contact-list {
    position: absolute; right: 24px; top: 206px; list-style: none;
    font-family: "Quicksand", sans-serif; font-size: 14px;
    line-height: 19.5px; color: var(--ink-soft); text-align: right;
  }
  .contact-list li { display: flex; align-items: center; justify-content: flex-end; gap: 8px; }
  .contact-icon { width: 14px; height: 14px; flex: none; }
  .services {
    position: absolute; top: 38px; left: 0; right: 0;
    text-align: center; color: var(--title-light);
    font-family: "Jura", sans-serif; font-weight: 400;
    font-size: 16.5px; line-height: 20.5px; letter-spacing: 0.4px;
    text-transform: uppercase;
  }
  .appointment {
    position: absolute; left: 34px; top: 209px;
    display: flex; align-items: center; gap: 6px;
    font-family: "Quicksand", sans-serif; font-size: 14px; color: var(--ink);
  }
  .appointment-field {
    position: absolute; top: 239px;
    font-family: "Quicksand", sans-serif; font-size: 14px; color: var(--ink);
  }
  .field-time { left: 54px; }
  .field-date { left: 250px; }
</style>
</head>
<body>
<main class="stage">

  <section class="card card-front" aria-label="Business card front">
    <svg class="card-art" viewBox="0 0 540 300" preserveAspectRatio="none" aria-hidden="true">
      <defs>
        <linearGradient id="front-silver" x1="0" y1="0" x2="1" y2="0">
          <stop offset="0" stop-color="#8e8e8e"/>
          <stop offset="0.3" stop-color="#d4d4d4"/>
          <stop offset="0.48" stop-color="#f0f0f0"/>
          <stop offset="0.72" stop-color="#b4b4b4"/>
          <stop offset="1" stop-color="#717171"/>
        </linearGradient>
        <linearGradient id="front-rim" x1="0" y1="0" x2="1" y2="0">
          <stop offset="0" stop-color="#9a9a9a"/>
          <stop offset="0.5" stop-color="#f4f4f4"/>
          <stop offset="1" stop-color="#a8a8a8"/>
        </linearGradient>
      </defs>
      <path d="M0,120 C180,160 380,185 540,168" fill="none" stroke="url(#front-rim)" stroke-width="5"/>
      <path d="M0,134 C180,174 380,198 540,182 L540,300 L0,300 Z" fill="url(#front-silver)"/>
    </svg>
    <h1 class="brand-title">BRIGHTMERE<br>DETAILING</h1>
    <p class="holder-name">Nora Pellworth</p>
    <p class="holder-address">4715 Quillbrook Rd<br>Ashcombe, VT 05871</p>
    <ul class="contact-list">
      <li>(802) 555-0148
        <svg class="contact-icon" viewBox="0 0 14 14" aria-hidden="true"><rect x="3.5" y="0.8" width="7" height="12.4" rx="1.3" fill="none" stroke="#111" stroke-width="1.4"/><line x1="6" y1="11" x2="8" y2="11" stroke="#111" stroke-width="1.2"/></svg>
      </li>
      <li>brightmeredetails@example.com
        <svg class="contact-icon" viewBox="0 0 14 14" aria-hidden="true"><rect x="0.8" y="2.5" width="12.4" height="9" fill="#111"/><path d="M1.5,3.5 L7,8 L12.5,3.5" fill="none" stroke="#ddd" stroke-width="1.1"/></svg>
      </li>
      <li>@brightmeredetailing
        <svg class="contact-icon" viewBox="0 0 14 14" aria-hidden="true"><rect x="1" y="1" width="12" height="12" rx="2" fill="#111"/></svg>
      </li>
      <li>@brightmeredetailing
        <svg class="contact-icon" viewBox="0 0 14 14" aria-hidden="true"><rect x="1" y="1" width="12" height="12" rx="2" fill="#111"/></svg>
      </li>
    </ul>
  </section>

  <section class="card card-back" aria-label="Business card back">
    <svg class="card-art" viewBox="0 0 540 300" preserveAspectRatio="none" aria-hidden="true">
      <defs>
        <linearGradient id="back-silver" x1="0" y1="0" x2="1" y2="0">
          <stop offset="0" stop-color="#8a8a8a"/>
          <stop offset="0.3" stop-color="#cfcfcf"/>
          <stop offset="0.5" stop-color="#eeeeee"/>
          <stop offset="0.75" stop-color="#a9a9a9"/>
          <stop offset="1" stop-color="#6a6a6a"/>
        </linearGradient>
        <linearGradient id="back-rim" x1="0" y1="0" x2="1" y2="0">
          <stop offset="0" stop-color="#9a9a9a"/>
          <stop offset="0.5" stop-color="#f4f4f4"/>
          <stop offset="1" stop-color="#a8a8a8"/>
        </linearGradient>
      </defs>
      <path d="M0,120 C180,160 380,185 540,168" fill="none" stroke="url(#back-rim)" stroke-width="5"/>
      <path d="M0,134 C180,174 380,198 540,182 L540,300 L0,300 Z" fill="url(#back-silver)"/>
    </svg>
    <p class="services">Minor paint correction;<br>Claying, multi-step buffing and polishing,<br>waxing, hand washes, interior cleaning and more!</p>
    <p class="appointment">
      <svg class="contact-icon" viewBox="0 0 14 14" aria-hidden="true"><rect x="1" y="2.2" width="12" height="11" fill="none" stroke="#111" stroke-width="1.3"/><rect x="1" y="2.2" width="12" height="3" fill="#111"/><line x1="4" y1="0.6" x2="4" y2="3" stroke="#111" stroke-width="1.3"/><line x1="10" y1="0.6" x2="10" y2="3" stroke="#111" stroke-width="1.3"/></svg>
      Your next appointment:
    </p>
    <p class="appointment-field field-time">Time:</p>
    <p class="appointment-field field-date">Date:</p>
  </section>

</main>
</body>
</html>
```